Building Company Business Card Design

Need a design for a business card:
It needs to have: Name, Phone, Social link, Website, email
i would also like a list of works we undertake:
-New Homes
-Extensions, Renovations & Bathrooms
-Decking, Carports, Sheds (Residential and Industrial)
-Carpentry
-Fences, Patios & Pergolas

Name, Phone, Social link, Website, email + details of services provided listed in description

```html
<!DOCTYPE html>
<html lang="en">
<head>
<meta charset="utf-8">
<title>Northgate Homes – Business Card</title>
<link rel="stylesheet" href="https://fonts.googleapis.com/css2?family=Archivo:wght@400;600;700;800&family=Archivo+Black&display=swap">
<style>
  :root {
    --orange-deep: #d9560f;
    --orange: #ee7d1c;
    --orange-light: #f6a532;
    --yellow: #f2c230;
    --red: #e4513a;
    --red-dark: #c73e2a;
    --paper: #f2f2f2;
    --ink: #3a3a3a;
    --ink-strong: #222;
    --stage: #ffffff;
  }
  * { box-sizing: border-box; margin: 0; padding: 0; }
  html, body { width: 1200px; height: 800px; overflow: hidden; }
  body {
    background: var(--stage);
    font-family: "Archivo", Arial, sans-serif;
    position: relative;
  }
  .card {
    position: absolute;
    left: 300px;
    width: 600px;
    height: 343px;
    border-radius: 18px;
    overflow: hidden;
    background: var(--paper);
    box-shadow: 0 6px 22px rgba(0,0,0,0.14);
  }
  .card--front { top: 36px; }
  .card--back { top: 418px; }

  /* front */
  .front-pattern {
    position: absolute; left: 0; top: 0; width: 232px; height: 100%;
    background: linear-gradient(135deg, var(--orange-light) 0%, var(--orange) 55%, var(--orange-deep) 100%);
  }
  .front-stripe-orange { position: absolute; left: 232px; top: 0; width: 8px; height: 100%; background: var(--orange); }
  .front-stripe-yellow { position: absolute; left: 244px; top: 0; width: 4px; height: 100%; background: var(--yellow); }
  .ribbon { position: absolute; left: 184px; top: 58px; width: 96px; height: 232px; }
  .ribbon-name {
    position: absolute; left: 232px; top: 174px;
    transform: translate(-50%, -50%) rotate(-90deg);
    display: flex; align-items: center; gap: 8px;
    white-space: nowrap;
    color: #fff; font-weight: 600; font-size: 13px; letter-spacing: 0.5px; line-height: 1.15;
  }
  .brand-square { width: 14px; height: 14px; background: var(--yellow); flex: none; }
  .contact {
    position: absolute; left: 292px; top: 100px; width: 280px;
  }
  .rule {
    height: 3px; width: 250px; margin-left: 14px;
    background: linear-gradient(90deg, transparent, var(--yellow) 20%, var(--yellow) 80%, transparent);
  }
  .contact-list { list-style: none; padding: 14px 0 14px 0; }
  .contact-list li {
    position: relative; padding-left: 16px;
    font-size: 14.5px; color: var(--ink); letter-spacing: 0.4px; line-height: 1.45;
  }
  .contact-list li::before {
    content: ""; position: absolute; left: 2px; top: 8px;
    width: 5px; height: 5px; border-radius: 50%; background: var(--ink-strong);
  }
  .contact-label { font-weight: 800; color: var(--ink-strong); }

  /* back */
  .services-title {
    position: absolute; left: 34px; top: 70px;
    font-family: "Archivo Black", "Archivo", sans-serif;
    color: var(--red); font-size: 44px; line-height: 0.98; letter-spacing: 0.5px;
  }
  .chevrons { position: absolute; left: 140px; top: 62px; width: 120px; height: 40px; }
  .title-underline {
    position: absolute; left: 30px; top: 172px; width: 240px; height: 3px;
    background: linear-gradient(90deg, transparent, var(--red) 15%, var(--red) 85%, transparent);
  }
  .services-list {
    position: absolute; left: 300px; top: 34px; list-style: none;
  }
  .services-list li {
    position: relative; padding-left: 14px;
    font-weight: 800; font-size: 12.5px; color: var(--ink-strong);
    letter-spacing: 0.3px; line-height: 1.55; text-transform: uppercase;
  }
  .services-list li::before {
    content: ""; position: absolute; left: 0; top: 8px;
    width: 4px; height: 4px; border-radius: 50%; background: var(--ink-strong);
  }
  .back-band-yellow { position: absolute; left: 0; top: 214px; width: 100%; height: 5px; background: var(--yellow); }
  .back-band-orange { position: absolute; left: 0; top: 222px; width: 100%; height: 6px; background: var(--orange); }
  .back-pattern {
    position: absolute; left: 0; top: 232px; width: 100%; height: 111px;
    background: linear-gradient(100deg, var(--orange) 0%, var(--orange-light) 45%, var(--orange) 75%, var(--orange-deep) 100%);
  }
  .name-tab {
    position: absolute; left: 190px; top: 192px; width: 230px; height: 86px;
    background: var(--red); border-radius: 12px 12px 0 0;
    display: flex; align-items: center; justify-content: center; gap: 8px;
    color: #fff; font-weight: 600; font-size: 13px; letter-spacing: 0.5px; line-height: 1.15;
    box-shadow: 0 3px 8px rgba(0,0,0,0.18);
  }
</style>
</head>
<body>

<section class="card card--front" aria-label="Business card front">
  <div class="front-pattern" role="img" aria-label="Orange geometric background with dot clusters and outlined shapes"></div>
  <div class="front-stripe-orange"></div>
  <div class="front-stripe-yellow"></div>
  <svg class="ribbon" viewBox="0 0 96 232" aria-hidden="true">
    <path d="M14 0 H90 V200 L48 232 L6 200 V12 Q6 0 14 0 Z" fill="var(--red)"/>
    <path d="M6 12 Q0 6 14 0 L14 14 Z" fill="var(--red-dark)"/>
  </svg>
  <div class="ribbon-name">
    <span class="brand-square"></span>
    <span>NORTHGATE HOMES<br>AND DEVELOPMENTS PTY LTD</span>
  </div>
  <div class="contact">
    <div class="rule"></div>
    <ul class="contact-list">
      <li><span class="contact-label">NAME</span>: YOUR NAME</li>
      <li><span class="contact-label">PHONE</span>: 0123456789</li>
      <li><span class="contact-label">EMAIL</span>: YOURMAIL@MAIL.EXAMPLE</li>
      <li><span class="contact-label">WEBSITE</span>:<br>WWW.WEBSITE.EXAMPLE</li>
      <li><span class="contact-label">SOCIAL</span>:<br>SOCIAL.EXAMPLE/YOUR NAME</li>
    </ul>
    <div class="rule"></div>
  </div>
</section>

<section class="card card--back" aria-label="Business card back">
  <h2 class="services-title">OUR<br>SERVICES</h2>
  <svg class="chevrons" viewBox="0 0 120 40" aria-hidden="true">
    <path d="M0 4 H22 L38 20 L22 36 H0 L16 20 Z" fill="var(--yellow)"/>
    <path d="M38 4 H60 L76 20 L60 36 H38 L54 20 Z" fill="var(--yellow)"/>
    <path d="M76 4 H98 L114 20 L98 36 H76 L92 20 Z" fill="var(--yellow)"/>
  </svg>
  <div class="title-underline"></div>
  <ul class="services-list">
    <li>New Homes</li>
    <li>Extensions, Renovations &amp; Bathrooms</li>
    <li>Decking, Carports, Sheds</li>
    <li>Carpentry</li>
    <li>Fences, Patios &amp; Pergolas</li>
  </ul>
  <div class="back-band-yellow"></div>
  <div class="back-band-orange"></div>
  <div class="back-pattern" role="img" aria-label="Orange geometric background with dot clusters and outlined shapes"></div>
  <div class="name-tab">
    <span class="brand-square"></span>
    <span>NORTHGATE HOMES<br>AND DEVELOPMENTS PTY LTD</span>
  </div>
</section>

</body>
</html>
```